Create a landing page for a new product market combination for an international software company

We are a software company being in the BtoB market for over 20 years. Our product is a software tool that allows for very flexible and versatile cost calculations for companies. We sell to all industries in over 40 countries with 500 clients. We have fairly recently seen a succesfull "competitor" (www.veltrani.com) come up in the niche market of IT costing. This competitor has launched an independent platform with regards to managing IT costs (www.QRSguild.org). In this independent platform standards are set, events are organised and books are written. Since our software can handle all type of costing questions we can en already do play a role in IT costing. We have therefore become a sponsor of the QRS guild. Besides that we came accross the opportunity to buy the URL: www.qrssoftware.com Which we did. We are now looking for a design on that landing page that communicates the fact that the visitor has landed with a company that have in depth knowledge on the QRS subject and provide an effective an affordable tooling for QRS. Currently the difference between the professionalism of our own website (www.pricelumen.com) and that of the competitor (www.veltrani.com) and the independent council (www.qrsguild.org). is too big.

Target Market(s)

BtB with large IT spend

Number of Pages Required

1 page

Colors

Designer to choose colors to be used in the design.

Requirements
Must have
• A proffessional look and feel
Should not have
• Definetely not too much information and wording

```html
<!DOCTYPE html>
<html lang="en">
<head>
<meta charset="utf-8">
<title>PriceLumen – Technology Business Management</title>
<link href="https://fonts.googleapis.com/css2?family=Roboto:wght@300;400;500;700;900&display=swap" rel="stylesheet">
<style>
  :root{
    --navy:#1f4a7e;
    --hero-top:#2a5d98;
    --hero-bottom:#1d4f8d;
    --orange:#f7931e;
    --dark:#241d18;
    --ink:#111111;
    --white:#ffffff;
    --muted:#cfc9c3;
    --accent-blue:#1e4a7d;
  }
  *{box-sizing:border-box;margin:0;padding:0}
  html,body{width:1200px;height:1200px;overflow:hidden;background:#fff;font-family:"Roboto",sans-serif}
  .page{position:relative;width:1200px;height:1200px;overflow:hidden}

  .hero{position:absolute;left:0;top:0;width:1200px;height:527px;
    background:linear-gradient(180deg,var(--hero-top),var(--hero-bottom))}
  .hero-art{position:absolute;inset:58px 0 0 0;
    background:radial-gradient(ellipse at 50% 70%,rgba(120,170,225,.35),rgba(30,80,140,0) 70%)}
  .navbar{position:absolute;left:0;top:0;width:1200px;height:58px;background:var(--navy)}
  .brand{position:absolute;left:140px;top:13px;color:var(--white);font-size:31px;font-weight:400;letter-spacing:-.5px;display:flex;align-items:center;gap:8px}
  .brand-mark{width:14px;height:14px;background:var(--white)}
  .nav-item{position:absolute;top:19px;transform:translateX(-50%);color:var(--white);font-size:13px;font-weight:500;white-space:nowrap}
  .nav-item.active{color:var(--orange)}
  .nav-item.active::after{content:"";position:absolute;left:-18px;right:-18px;top:24px;height:2px;background:var(--orange)}

  .hero-title{position:absolute;left:0;width:1200px;top:170px;text-align:center;color:var(--white);
    font-weight:900;font-size:44px;line-height:51px;letter-spacing:1.5px}
  .search{position:absolute;left:413px;top:309px;width:376px;height:44px;background:var(--white);border-radius:22px}
  .search-icon{position:absolute;left:19px;top:13px}
  .search-text{position:absolute;left:46px;top:14px;font-size:13px;color:#666}
  .go{position:absolute;left:690px;top:306px;width:99px;height:50px;border-radius:25px;background:var(--orange);
    color:var(--white);font-weight:500;font-size:16px;letter-spacing:1px;text-align:center;line-height:50px;box-shadow:0 3px 8px rgba(0,0,0,.2)}

  .section-title{position:absolute;left:0;width:1200px;top:568px;text-align:center;font-size:27px;font-weight:900;color:var(--ink);letter-spacing:.5px}
  .section-title span{color:var(--accent-blue)}
  .stat{position:absolute;width:240px;transform:translateX(-50%);text-align:center}
  .stat svg{display:block;margin:0 auto}
  .stat-label{margin-top:28px;font-size:16px;font-weight:500;line-height:20px;color:var(--ink)}

  .band{position:absolute;left:0;top:920px;width:1200px;height:280px;background:var(--dark)}
  .spine{position:absolute;left:565px;top:899px;width:68px;height:301px;background:var(--orange)}
  .spine-text{position:absolute;left:0;width:68px;top:54px;text-align:center;color:var(--white);font-weight:700;font-size:14px;line-height:15.8px}
  .card-img{position:absolute;width:177px;height:164px;background:var(--white)}
  .card-img .fill{position:absolute;inset:14px;border-radius:4px}
  .card-title{position:absolute;color:var(--white);font-size:16px;font-weight:700;letter-spacing:1px}
  .card-text{position:absolute;color:var(--muted);font-size:12px;line-height:19px;width:230px;font-weight:300}
  .link{position:absolute;height:2px;background:var(--orange)}
  .link::after{content:"";position:absolute;top:-5px;width:12px;height:12px;border-radius:50%;background:var(--orange)}
  .link.left::after{right:-6px}
  .link.right::after{left:-6px}
</style>
</head>
<body>
<div class="page">
  <header class="hero">
    <div class="hero-art" role="img" aria-label="Chalk-style sketches of charts, graphs and business ideas on blue"></div>
    <nav class="navbar">
      <div class="brand"><span class="brand-mark"></span>PriceLumen</div>
      <span class="nav-item active" style="left:461px">Home</span>
      <span class="nav-item" style="left:532px">Product</span>
      <span class="nav-item" style="left:610px">Markets</span>
      <span class="nav-item" style="left:692px">Company</span>
      <span class="nav-item" style="left:779px">Partners</span>
      <span class="nav-item" style="left:863px">Events</span>
      <span class="nav-item" style="left:947px">Supports</span>
      <span class="nav-item" style="left:1035px">Contact</span>
    </nav>
    <h1 class="hero-title">TECHNOLOGY BUSINESS<br>MANAGEMENT</h1>
    <div class="search">
      <svg class="search-icon" width="18" height="18" viewBox="0 0 18 18"><circle cx="7.5" cy="7.5" r="6" fill="none" stroke="#888" stroke-width="1.6"/><line x1="12" y1="12" x2="17" y2="17" stroke="#888" stroke-width="1.6"/></svg>
      <span class="search-text">Serach here..</span>
    </div>
    <div class="go">GO</div>
  </header>

  <h2 class="section-title">MANAGE TECHNOLOGY AS A BUSINESS: <span>QRS</span></h2>

  <div class="stat" style="left:336px;top:633px">
    <svg width="130" height="130" viewBox="0 0 130 130"><circle cx="65" cy="65" r="63" fill="none" stroke="#7a5a3a" stroke-width="1"/><circle cx="65" cy="65" r="63" fill="none" stroke="var(--orange)" stroke-width="3" stroke-dasharray="336 400" transform="rotate(-60 65 65) scale(1 -1) translate(0 -130)"/><text x="65" y="74" text-anchor="middle" font-family="Roboto,sans-serif" font-size="23" fill="var(--orange)">85%</text></svg>
    <div class="stat-label">Foster a Business<br>Culture in IT</div>
  </div>
  <div class="stat" style="left:601px;top:633px">
    <svg width="130" height="130" viewBox="0 0 130 130"><circle cx="65" cy="65" r="63" fill="none" stroke="#7a5a3a" stroke-width="1"/><circle cx="65" cy="65" r="63" fill="none" stroke="var(--orange)" stroke-width="3" stroke-dasharray="356 400" transform="rotate(-72 65 65) scale(1 -1) translate(0 -130)"/><text x="65" y="74" text-anchor="middle" font-family="Roboto,sans-serif" font-size="23" fill="var(--orange)">90%</text></svg>
    <div class="stat-label">Enable the right<br>business conversations</div>
  </div>
  <div class="stat" style="left:893px;top:633px">
    <svg width="130" height="130" viewBox="0 0 130 130"><circle cx="65" cy="65" r="63" fill="none" stroke="#7a5a3a" stroke-width="1"/><circle cx="65" cy="65" r="63" fill="none" stroke="var(--orange)" stroke-width="3" stroke-dasharray="356 400" transform="rotate(-72 65 65) scale(1 -1) translate(0 -130)"/><text x="65" y="74" text-anchor="middle" font-family="Roboto,sans-serif" font-size="23" fill="var(--orange)">90%</text></svg>
    <div class="stat-label">Develop Sound<br>Fiscal Disciplines</div>
  </div>

  <section class="band">
    <div class="card-img" style="left:67px;top:73px"><div class="fill" role="img" aria-label="Illustration of three linked blue chain loops" style="background:linear-gradient(135deg,#bfe3f5,#3aa7de)"></div></div>
    <h3 class="card-title" style="left:263px;top:80px">POSITION FOR VALUE</h3>
    <p class="card-text" style="left:263px;top:115px">Define what you deliver in terms of business capabilities that are understood and valued by your business unit partners, so you can work together to improve business outcomes.</p>
    <div class="link left" style="left:499px;top:147px;width:51px"></div>

    <div class="card-img" style="left:708px;top:73px"><div class="fill" role="img" aria-label="Illustration of a rising bar chart with a light bulb" style="background:linear-gradient(135deg,#2a7f73,#8cc63f)"></div></div>
    <h3 class="card-title" style="left:904px;top:80px">CONTINUOUSLY IMPROVE</h3>
    <p class="card-text" style="left:904px;top:116px">Execute a strategic roadmap for QRS maturity by integrating QRS into your day-to-day processes and thinking, so that QRS drives every value conversation with your peers.</p>
    <div class="link right" style="left:652px;top:174px;width:50px"></div>

    <div class="card-img" style="left:67px;top:260px">
      <svg width="177" height="164" viewBox="0 0 177 164"><g fill="rgba(30,74,125,.2)" stroke="#1e4a7d" stroke-width="1.5"><circle cx="63" cy="70" r="40"/><circle cx="106" cy="70" r="40"/><circle cx="84" cy="105" r="40"/></g></svg>
    </div>
    <h3 class="card-title" style="left:263px;top:267px">CREATE TRANSPARENCY</h3>
    <p class="card-text" style="left:263px;top:302px;font-size:13px">Translate your spending, consumption, and capacity into meaningful perspectives for technology and business decision-makers</p>
    <div class="link left" style="left:499px;top:327px;width:51px"></div>

    <div class="card-img" style="left:708px;top:260px"><div class="fill" role="img" aria-label="Illustration of analytics screens and a magnifier" style="background:linear-gradient(135deg,#e6eef5,#c94a5a)"></div></div>
    <h3 class="card-title" style="left:904px;top:267px">SHAPE BUSINESS DEMAND</h3>
  </section>

  <div class="spine"><div class="spine-text">F<br>O<br>S<br>T<br>E<br>R<br><br>A<br><br>B<br>U<br>S<br>I<br>N<br>E<br>S<br>S</div></div>
</div>
</body>
</html>
```